Catalogue Design Project

we are college are would like have a,

College Hand out booklet, infomation book.

this book will be used for marketing,branding, given to new students, business, all information about our college including course information, college information, eg. a university ingo book A4 in size.
we would like to have the cover pages and all internal pages designed, then the content we can do locally.

Industry/Entity Type

University

```html
<!DOCTYPE html>
<html lang="en">
<head>
<meta charset="utf-8">
<title>Harwell College – A Bright Future</title>
<link href="https://fonts.googleapis.com/css2?family=Bebas+Neue&family=Didact+Gothic&family=Cinzel:wght@700&display=swap" rel="stylesheet">
<style>
  :root {
    --stage: #5d5d5f;
    --cover-blue: #b2d2e8;
    --cover-blue-deep: #9cc3df;
    --navy: #1d4f9c;
    --green: #1f8a3c;
    --green-light: #8cc63f;
    --ink: #1d1d1d;
    --link: #2f6db5;
    --white: #ffffff;
  }
  * { box-sizing: border-box; margin: 0; padding: 0; }
  html, body {
    width: 1184px; height: 1200px; overflow: hidden;
    background: var(--stage);
  }
  .cover {
    position: absolute; left: 238px; top: 100px;
    width: 708px; height: 1000px;
    background: linear-gradient(180deg, var(--cover-blue) 0%, var(--cover-blue-deep) 100%);
    overflow: hidden;
  }
  .cover-art { position: absolute; inset: 0; width: 708px; height: 1000px; }
  .brand {
    position: absolute; left: 450px; top: 450px; width: 240px;
    display: flex; align-items: center; gap: 10px;
    font-family: "Cinzel", serif; font-weight: 700; font-size: 22px;
    color: var(--navy);
  }
  .brand-dot { width: 18px; height: 18px; border-radius: 50%; background: var(--navy); flex: none; }
  .headline-band {
    position: absolute; left: 0; top: 540px; width: 708px; height: 82px;
    background: linear-gradient(90deg, var(--white) 0%, var(--white) 65%, rgba(255,255,255,0) 95%);
  }
  .headline {
    position: absolute; left: 28px; top: 548px;
    font-family: "Bebas Neue", sans-serif; font-size: 76px; line-height: 1;
    color: var(--navy); letter-spacing: 0.5px;
  }
  .tagline-band {
    position: absolute; left: 0; top: 622px; width: 708px; height: 48px;
    background: linear-gradient(90deg, var(--green) 0%, var(--green) 30%, var(--green-light) 65%, rgba(140,198,63,0) 90%);
  }
  .tagline {
    position: absolute; left: 30px; top: 626px;
    font-family: "Didact Gothic", sans-serif; font-size: 34px; line-height: 1.15;
    color: var(--white);
  }
  .contact {
    position: absolute; left: 56px; top: 840px;
    font-family: "Didact Gothic", sans-serif; font-size: 16px; line-height: 1.45;
    color: var(--ink);
  }
  .contact .web { color: var(--link); margin-top: 6px; }
</style>
</head>
<body>
  <main class="cover">
    <svg class="cover-art" viewBox="0 0 708 1000" aria-hidden="false">
      <defs>
        <linearGradient id="photo-tone" x1="0" y1="0" x2="1" y2="1">
          <stop offset="0" stop-color="#5f7d3a"/>
          <stop offset="0.45" stop-color="#7fa54a"/>
          <stop offset="0.75" stop-color="#3f5f9a"/>
          <stop offset="1" stop-color="#a7c47a"/>
        </linearGradient>
      </defs>
      <path class="cover-photo" role="img" aria-label="Photo: smiling student lying on the grass reading a book"
            fill="url(#photo-tone)"
            d="M0 0 H708 V170 C600 220 520 250 420 330 C340 400 220 420 120 380 C70 360 30 340 0 330 Z"/>
      <path class="wave-line" fill="none" stroke="#ffffff" stroke-opacity="0.8" stroke-width="1.5"
            d="M0 340 C60 365 120 395 200 405 C300 415 360 380 430 330 C520 265 620 215 708 185"/>
      <path class="wave-line" fill="none" stroke="#ffffff" stroke-opacity="0.6" stroke-width="1"
            d="M0 380 C80 420 170 445 260 440 C360 435 430 380 520 320 C590 275 650 245 708 230"/>
    </svg>

    <div class="brand"><span class="brand-dot"></span>Harwell College</div>

    <div class="headline-band"></div>
    <h1 class="headline">A Bright Future</h1>
    <div class="tagline-band"></div>
    <p class="tagline">We get you ready</p>

    <address class="contact" style="font-style:normal">
      <div>Enquiry us today!</div>
      <div>+617 3480 2265</div>
      <div>enquiries@harwellcollege.net.au</div>
      <div class="web">www.harwellcollege.net.au</div>
    </address>
  </main>
</body>
</html>
```